Tallpine Facility Upkeep Systems

I need a full website built that must work on destkop and mobile. I have the logo's and will upload them however some stock industrial photos will be required. I will be hosting it on wix/godaddy for use with dynamics 365. Pretty simple requirements:

*Splash page
*What We Do
*How We do it
*Who Are We?
*Software
*Partnerships
*Contact: Includes twitter/insta and email/addy/phone

The site should be more scroll oriented with fewer tabs to allow for a improved mobile experience.
We're also looking for ways to improve our inbound marketing and would want to include various areas to get in touch /or collect their info. Look to www.kelnarova.com as an example of inbound marketing.
Images should be representative of the verticals we're focused on.

I have most of the content.

Target Market(s)

Asset intensive industries: Mining, Oil and Gas, Forest Products and Manufacturing.

Industry/Entity Type

Asset Management

Coding

Coded - Design and coding required

Number of Pages Required

5+ page

Font styles to use
Sans Serif

Requirements
Must have
• Must be easy to view and navigate on mobile and desktop.
Nice to have
• Employee/Customer portal.
Should not have
• Anything that will not display well in a mobile environment.

```html
<!DOCTYPE html>
<html lang="en">
<head>
<meta charset="utf-8">
<title>Tallpine Facility Upkeep Systems</title>
<link href="https://fonts.googleapis.com/css2?family=Montserrat:wght@400;600;700;800&family=Open+Sans:wght@400;600;700&display=swap" rel="stylesheet">
<style>
:root{
  --green:#8dbe3f;
  --green-dark:#6f9730;
  --olive:#5c6b45;
  --teal:#2c8a8c;
  --teal-light:#7cc3c2;
  --ink:#2f3433;
  --grey:#6b6f70;
  --mist:#e6e9e7;
  --white:#ffffff;
}
*{box-sizing:border-box;margin:0;padding:0}
html,body{width:1200px;height:3072px;overflow:hidden;background:var(--white)}
body{font-family:"Open Sans",Arial,sans-serif;color:var(--ink);position:relative}
.site-header{height:80px;display:flex;align-items:center;justify-content:space-between;padding:0 40px;background:var(--white)}
.brand{display:flex;align-items:center;gap:12px;font-family:"Montserrat",Arial,sans-serif;font-weight:800;font-size:30px;color:var(--green-dark);letter-spacing:1px}
.brand-mark{width:22px;height:22px;background:var(--green)}
.main-nav{display:flex;gap:34px;font-family:"Montserrat",Arial,sans-serif;font-size:16px;color:var(--grey)}
.hero{height:740px;position:relative;background:linear-gradient(135deg,#4c5254 0%,#8a9093 45%,#c9ccc9 70%,#6d7275 100%);display:flex;align-items:flex-start;justify-content:center}
.hero-intro{position:relative;margin-top:90px;width:1060px;text-align:center;color:var(--white);font-family:"Montserrat",Arial,sans-serif;font-weight:700;font-size:37px;line-height:49px;letter-spacing:1.5px;text-shadow:0 2px 6px rgba(0,0,0,.35)}
.benefits{height:340px;background:var(--green);display:flex;align-items:center;justify-content:center}
.benefits ul{list-style:none;text-align:center;color:var(--white);font-weight:700;font-size:26px;line-height:40px}
.benefits li::before{content:"• "}
.audience{display:grid;grid-template-columns:400px 400px 400px;height:420px}
.audience-col{display:flex;flex-direction:column}
.audience-col h3{height:90px;background:var(--olive);color:var(--white);font-size:22px;font-weight:700;padding:16px 28px;line-height:28px;display:flex;align-items:center}
.audience-col ul{flex:1;background:var(--green);list-style:none;padding:30px 28px;color:var(--white);font-weight:600;font-size:22px;line-height:30px}
.audience-col li::before{content:"• "}
.approach{padding-top:140px;text-align:center}
.section-box{display:inline-block;border:4px solid var(--green);padding:12px 44px;font-family:"Montserrat",Arial,sans-serif;font-weight:600;font-size:52px;letter-spacing:2px;color:var(--ink)}
.approach-sub{margin-top:12px;font-family:"Montserrat",Arial,sans-serif;font-weight:700;font-size:38px;color:var(--ink)}
.approach-grid{display:grid;grid-template-columns:300px 300px 300px;gap:40px;justify-content:center;margin-top:60px;text-align:left}
.pillar-title{height:82px;background:var(--green);color:var(--white);font-family:"Montserrat",Arial,sans-serif;font-weight:600;font-size:33px;line-height:34px;display:flex;align-items:center;justify-content:center;text-align:center}
.pillar-list{list-style:none;margin-top:28px;font-family:"Montserrat",Arial,sans-serif;font-size:40px;line-height:48px;color:var(--ink)}
.pillar-list li{padding-left:34px;text-indent:-34px}
.pillar-list li::before{content:"• "}
.framing{position:absolute;top:2420px;left:0;width:1200px;height:170px;background:var(--green);text-align:center;color:var(--white);font-family:"Montserrat",Arial,sans-serif;font-weight:700;padding-top:30px}
.framing h2{font-size:52px;letter-spacing:2px;line-height:58px}
.framing p{font-size:42px;line-height:50px}
.framing-graphic{position:absolute;top:2610px;left:80px;width:1040px;height:430px;background:linear-gradient(90deg,var(--mist) 0%,var(--mist) 50%,var(--teal-light) 62%,var(--teal) 100%)}
</style>
</head>
<body>
<header class="site-header">
  <div class="brand"><span class="brand-mark"></span>TALLPINE</div>
  <nav class="main-nav"><span>What We Do</span><span>How We do it</span><span>Who Are We</span><span>Software</span><span>Partnerships</span><span>Contact</span></nav>
</header>

<section class="hero" role="img" aria-label="Photograph of hands working at a laptop on a desk">
  <p class="hero-intro">Tallpine Facility Upkeep Systems is a boutique firm specializing in maintenance and reliability, supply chain, business intelligence and program management for asset intensive industries. We represent the finest people, process and technology tools to achieve greater results.</p>
</section>

<section class="benefits">
  <ul>
    <li>Improved planned &amp; scheduled maintenance</li>
    <li>Uptime improvements</li>
    <li>Longevity and safety of equipment</li>
    <li>Optimized asset performance</li>
    <li>Administrative savings</li>
    <li>Improved inventory levels</li>
    <li>Skills portability, increased employee morale</li>
  </ul>
</section>

<section class="audience">
  <div class="audience-col">
    <h3>Executive &amp; Operations Managers</h3>
    <ul>
      <li>More reliable operations.</li>
      <li>Increased efficiency and profitability.</li>
      <li>Reduced and reliable maintenance costs.</li>
      <li>Reduced liability/risk.</li>
      <li>Manage by knowledge (reduce surprises).</li>
      <li>Better Budgeting.</li>
    </ul>
  </div>
  <div class="audience-col">
    <h3>Maintenance Managers</h3>
    <ul>
      <li>Better information.</li>
      <li>Better organization, decisions and justifications.</li>
      <li>Identify where to spend money most effectively.</li>
    </ul>
  </div>
  <div class="audience-col">
    <h3>Maintenance Workers</h3>
    <ul>
      <li>Easier to prevent messes before they happen.</li>
      <li>Get information, not the runaround.</li>
      <li>Spend time working on the right things.</li>
    </ul>
  </div>
</section>

<section class="approach">
  <div class="section-box">HOW WE DO IT</div>
  <p class="approach-sub">Project approach</p>
  <div class="approach-grid">
    <div>
      <div class="pillar-title">Three Pillars</div>
      <ul class="pillar-list"><li>Maintenance &amp; Reliability</li><li>Inventory &amp; Stores</li><li>Procurement &amp; Payables</li></ul>
    </div>
    <div>
      <div class="pillar-title">Three Phases</div>
      <ul class="pillar-list"><li>Pre-Feasibility</li><li>Feasibility</li><li>Execution</li></ul>
    </div>
    <div>
      <div class="pillar-title">Three Dimensions</div>
      <ul class="pillar-list"><li>People &amp; Process</li><li>Physical</li><li>Technical</li></ul>
    </div>
  </div>
</section>

<section class="framing">
  <h2>MAINTENANCE</h2>
  <p>AND RELIABILITY FRAMING</p>
</section>

<div class="framing-graphic" role="img" aria-label="Infographic relating maintenance capabilities to their value proposition and the role of maintenance and reliability"></div>
</body>
</html>
```